Mediakit / brochure for Dutch Travel Blog

About our company:
• Bolderwijk.nl is a Travel- & influence network for independent travellers, outdoor geeks, culture lovers & adventure seekers.
• We don’t sell trips by ourself, we inspire other to travel.
• It’s all about travel inspiration.

About the media kit / brochure:
• The media kit itself must be a travel experience / inspiration.
• Colourful and clean design.
• Use the colours of our new logo
• Use our icons (marker, worldmap) in the design
• Use the style of our website.
• All the text in the media kit must be adjustable by us
• Page format: A4
• Number of pages: 6
• It must be printable as a brochure (for presentations)
• We also need a .pdf version of the brochure (for emailing it to our partners)
• Logo kit added: (1a) + (1b) + (1c) Logo sourcefile

Content of the media kit / brochure
• 6 pages
o (1) Front page
o (2) About Us
o (3) Stats / Companies work with
o (4) Advertising
o (5) Back page
o (6) Our contributors

• Example is attached: (2) example of a brochure with 5 pages A4 (don’t like the design of this example for our media kit, but just to show the idea of the 5 pages).

Maybe use a big travel photo that covers all pages?

For detailed information, I attached the document 'Design brochure Bolderwijk (version 2)'.
Updates

Hello designers,Small update for the Cover Page:- Please use one of the images from the attachment I added in the Brief Design: "URL of images for cover.txt"- Use this text "Travel- & influence network for independent travelers, outdoor geeks, culture lovers & adventure seekers."- Add the text MEDIA KIT (remove "2017: )Thanks.Hendrik Added Thursday, January 5, 2017

Target Market(s)

The mediakit / brochure is for our partners (travel organisations, airline companies, PR companies and big brands like Pale Timber Co and Vesko).

And the readers of our website are independent travellers, outdoor geeks and adventure seekers. So the theme of the Mediakit must be 'travel inspiration'.

Industry/Entity Type

Travel Industry

Requirements
Must have
• • The media kit itself must be a travel experience / inspiration.
• • Colourful and clean design.
• • Use the colours of our new logo
• • Use our icons (marker, worldmap) in the design
• • Use the style of our website.
• • All the text in the media kit must be adjustable by us
• • Page format: A4
• • Number of pages: 6
• • It must be printable as a brochure (for presentations)
• • We also need a .pdf version of the brochure (for emailing it to our partners)

```html
<!DOCTYPE html>
<html lang="en">
<head>
<meta charset="utf-8">
<title>Bolderwijk Media Kit – Spread</title>
<link href="https://fonts.googleapis.com/css2?family=Open+Sans:wght@400;600;700&display=swap" rel="stylesheet">
<style>
  :root {
    --stage: #343434;
    --blue: #1a79c2;
    --blue-deep: #0f5ea6;
    --orange: #f39200;
    --amber: #f5a623;
    --ink: #222;
    --text: #333;
    --white: #fff;
    --grey: #cfcfcf;
    --table-bg: rgba(38, 38, 40, 0.88);
    --lime: #b5d334;
    --cyan: #2bb8d8;
    --red: #e3262c;
    --dark: #333;
  }
  * { box-sizing: border-box; margin: 0; padding: 0; }
  html, body { width: 1200px; height: 680px; overflow: hidden; }
  body {
    background: var(--stage);
    font-family: "Open Sans", Arial, sans-serif;
    color: var(--text);
    position: relative;
  }
  .spread {
    position: absolute;
    left: 20px; top: 67px;
    width: 1160px; height: 546px;
    display: flex;
  }
  .page { position: relative; width: 387px; height: 546px; overflow: hidden; background: var(--white); }
  .page--middle { width: 386px; }
  .page__frame { position: absolute; inset: 0; width: 100%; height: 100%; }
  .abs { position: absolute; }

  /* Left page */
  .quote { left: 0; right: 0; top: 16px; text-align: center; font-size: 20px; color: var(--ink); font-weight: 400; }
  .quote__mark { font-weight: 700; font-size: 30px; vertical-align: -6px; margin: 0 6px; }
  .section-title { color: var(--blue); font-weight: 700; font-size: 18px; letter-spacing: 0.2px; }
  .traffic-title { right: 39px; top: 106px; text-align: right; color: var(--orange); font-weight: 700; font-size: 10px; line-height: 11px; }
  .label { font-size: 7px; color: var(--text); text-transform: uppercase; }
  .gender__row { display: flex; align-items: center; gap: 4px; font-size: 8.5px; font-weight: 700; height: 13px; }
  .dot { width: 7px; height: 7px; border-radius: 50%; }
  .dot--female { background: #e8347e; }
  .dot--male { background: var(--blue); }
  .pct-female { color: #e8347e; }
  .pct-male { color: var(--blue); }
  .age-chart { left: 161px; top: 156px; width: 130px; }
  .age-bar { display: flex; align-items: center; height: 10px; gap: 4px; font-size: 6.5px; font-weight: 600; white-space: nowrap; }
  .age-bar__fill { height: 7px; font-size: 4px; color: var(--white); padding-left: 2px; line-height: 7px; overflow: hidden; }
  .social-stats { left: 292px; top: 140px; }
  .social-stats__row { display: flex; align-items: center; gap: 4px; height: 23px; font-size: 7.5px; font-weight: 600; color: var(--ink); white-space: nowrap; }
  .square { width: 9px; height: 9px; border-radius: 2px; }
  .map { left: 38px; top: 186px; width: 108px; height: 60px; }
  .badge { left: 95px; top: 183px; background: var(--red); color: var(--white); font-size: 7.5px; font-weight: 700; padding: 1px 3px; }
  .countries { left: 100px; top: 198px; width: 30px; font-size: 4px; color: var(--white); text-align: center; line-height: 5px; }
  .metric { left: 200px; width: 148px; display: flex; justify-content: space-between; align-items: baseline; }
  .metric__value { font-size: 9.5px; font-weight: 700; color: var(--blue-deep); }
  .metric__label { font-size: 9px; font-weight: 700; color: var(--orange); text-align: right; line-height: 8px; }
  .metric__label small { display: block; font-size: 3.5px; color: var(--text); font-weight: 400; }
  .sub-title { color: var(--blue); font-size: 11px; font-weight: 600; }
  .body-copy { font-size: 5.8px; line-height: 7.8px; color: var(--text); text-align: justify; }
  .logo-strip { left: 39px; width: 309px; height: 41px; background: var(--white); display: flex; align-items: center; justify-content: space-around; padding: 0 8px; box-shadow: 0 0 2px rgba(0,0,0,.08); }
  .partner { font-weight: 700; font-size: 9px; color: var(--blue-deep); white-space: nowrap; }
  .partner--dark { color: var(--ink); }
  .partner--red { color: #9b1c1c; }
  .partner--green { color: #1a9a6c; }

  /* Middle page */
  .rate-card { left: 20px; top: 0; width: 241px; height: 331px; background: var(--table-bg); }
  .rate { position: absolute; left: 22px; width: 192px; height: 18px; display: grid; grid-template-columns: 118px 1fr; border: 1px solid rgba(255,255,255,.25); font-size: 8.5px; color: var(--white); white-space: nowrap; }
  .rate--wide { grid-template-columns: 134px 1fr; }
  .rate--note { grid-template-columns: 80px 1fr; }
  .rate > span { display: flex; align-items: center; padding-left: 12px; }
  .rate__price { color: var(--amber); border-left: 1px solid rgba(255,255,255,.25); padding-left: 8px !important; }
  .rate__price small { font-size: 5px; margin-top: 3px; }
  .rate__note { font-size: 5px; justify-content: center; padding-left: 0 !important; }
  .rate__small { font-size: 5px; margin-left: 2px; margin-top: 2px; }
  .rate--header { display: flex; align-items: center; padding-left: 12px; color: var(--amber); }

  /* Right page */
  .sponsor-title { left: 39px; top: 108px; color: var(--blue); font-size: 20px; font-weight: 700; }
  .sponsor-intro { left: 39px; top: 137px; width: 310px; }
  .sponsor-lead { left: 39px; top: 159px; font-size: 9.5px; color: var(--ink); }
  .services { left: 39px; top: 179px; width: 310px; list-style: none; }
  .service { margin-bottom: 7px; }
  .service__title { display: flex; align-items: center; gap: 6px; color: var(--blue); font-size: 9.5px; font-weight: 600; line-height: 11px; }
  .service__dot { width: 8px; height: 8px; border-radius: 50%; background: var(--cyan); }
  .pricing-note { right: 38px; top: 469px; font-size: 7.5px; font-weight: 700; color: var(--ink); }
</style>
</head>
<body>
<main class="spread">

  <!-- Page: audience and partners -->
  <section class="page page--left">
    <svg class="page__frame" viewBox="0 0 387 546" preserveAspectRatio="none" aria-hidden="true">
      <defs>
        <linearGradient id="sunset" x1="0" y1="0" x2="0" y2="1">
          <stop offset="0" stop-color="#e4603a"/>
          <stop offset=".55" stop-color="#f29a4a"/>
          <stop offset="1" stop-color="#8a5a3c"/>
        </linearGradient>
        <linearGradient id="floorGrey" x1="0" y1="0" x2="0" y2="1">
          <stop offset="0" stop-color="#e6e6e6"/>
          <stop offset="1" stop-color="#bdbdbd"/>
        </linearGradient>
      </defs>
      <rect x="0" y="0" width="387" height="140" fill="url(#sunset)" role="img" aria-label="Photo of a sunset sky over a forest edge"/>
      <path d="M0,96 C110,62 260,56 387,76 L387,84 C260,64 110,70 0,104 Z" fill="#fff" opacity=".85"/>
      <path d="M0,104 C110,70 260,64 387,84 L387,100 C260,82 110,88 0,114 Z" fill="var(--blue)"/>
      <path d="M0,114 C110,88 260,82 387,100 L387,546 L0,546 Z" fill="#fff"/>
      <path d="M0,444 C130,498 270,510 387,498 L387,546 L0,546 Z" fill="url(#floorGrey)"/>
      <path d="M0,444 C130,498 270,510 387,498 L387,508 C270,520 130,512 0,462 Z" fill="var(--blue)"/>
      <path d="M0,470 C130,520 270,530 387,518 L387,521 C270,533 130,524 0,474 Z" fill="#9a9a9a"/>
    </svg>

    <h1 class="abs quote"><span class="quote__mark">“</span>Let’s work together!<span class="quote__mark">”</span></h1>

    <h2 class="abs section-title" style="left:38px; top:112px;">AUDIENCE OVERVIEW</h2>
    <h3 class="abs traffic-title">TRAFFIC &amp;<br>SOCIAL MEDIA</h3>

    <span class="abs label" style="left:38px; top:140px;">Gender</span>
    <div class="abs gender" style="left:88px; top:140px;">
      <div class="gender__row"><span class="dot dot--female"></span><span class="pct-female">66%</span></div>
      <div class="gender__row"><span class="dot dot--male"></span><span class="pct-male">34%</span></div>
    </div>

    <span class="abs label" style="left:161px; top:140px;">Age</span>
    <div class="abs age-chart">
      <div class="age-bar"><span class="age-bar__fill" style="width:28px;background:var(--lime)">18-24</span>11%</div>
      <div class="age-bar"><span class="age-bar__fill" style="width:84px;background:var(--blue)">25-34</span>30%</div>
      <div class="age-bar"><span class="age-bar__fill" style="width:105px;background:var(--orange)">35-44</span>36%</div>
      <div class="age-bar"><span class="age-bar__fill" style="width:33px;background:var(--cyan)">45-54</span>12%</div>
      <div class="age-bar"><span class="age-bar__fill" style="width:20px;background:var(--red)">55-64</span>9%</div>
      <div class="age-bar"><span class="age-bar__fill" style="width:5px;background:var(--dark)"></span>65+ 2%</div>
    </div>

    <div class="abs social-stats">
      <div class="social-stats__row"><span class="square" style="background:#3b5a98"></span>Friendbook 30.000</div>
      <div class="social-stats__row"><span class="square" style="background:#1da1f2"></span>Chirper 5200</div>
      <div class="social-stats__row"><span class="square" style="background:#c13584"></span>Snapgram 7000</div>
    </div>

    <span class="abs label" style="left:38px; top:172px;">Location</span>
    <svg class="abs map" viewBox="0 0 108 60" role="img" aria-label="World map with visited countries highlighted">
      <rect width="108" height="60" rx="8" fill="var(--blue)"/>
    </svg>
    <span class="abs badge">81%</span>
    <span class="abs countries">Countries<br>visited</span>

    <div class="abs metric" style="top:210px;">
      <span class="metric__value">240.000</span>
      <span class="metric__label">PAGE VIEWS<small>*MONTHLY</small></span>
    </div>
    <div class="abs metric" style="top:227px;">
      <span class="metric__value">115.000</span>
      <span class="metric__label">UNIQUE VISITORS<small>*MONTHLY</small></span>
    </div>

    <h3 class="abs sub-title" style="left:38px; top:250px;">Companies We Work With</h3>
    <p class="abs body-copy" style="left:38px; top:266px; width:310px;">Wondering how to transform your product from a commodity into an experience? Not sure how to leverage the power of social media and connect with your target demographic? Need help aligning your branding with your company values? Whether you are a tourism board, travel company, property, or product, we can help. We work with more than 100 travel- and brand partners</p>

    <h3 class="abs sub-title" style="left:38px; top:304px;">Travel Partners</h3>
    <p class="abs body-copy" style="left:38px; top:320px; width:310px;">We have worked with some of the world’s top travel companies &amp; destinations to help them achieve their goals. They leverage our authority and expertise in social media promotion, cross-marketing campaigns and unique content creation to showcase their offerings.</p>

    <div class="abs logo-strip" style="top:354px;">
      <span class="partner">Skyline Air</span>
      <span class="partner partner--red">Wanderloop Tours</span>
      <span class="partner partner--green">Isla Sol</span>
      <span class="partner">Farescope</span>
    </div>

    <h3 class="abs sub-title" style="left:38px; top:400px;">Brand Partners</h3>
    <p class="abs body-copy" style="left:38px; top:416px; width:310px;">Bolderwijk reaches a niche audience of travellers passionate about unique experiences and amazing products. We have helped countless brands, from fashion labels to major technology corporations, bring their products to The Netherlands and reach their target consumers.</p>

    <div class="abs logo-strip" style="top:448px;">
      <span class="partner partner--dark">Vesko</span>
      <span class="partner partner--dark">Routewise</span>
      <span class="partner partner--dark">Actiocam</span>
      <span class="partner partner--dark">Pale Timber Co</span>
    </div>
  </section>

  <!-- Page: advertising rates -->
  <section class="page page--middle">
    <svg class="page__frame" viewBox="0 0 386 546" preserveAspectRatio="none" role="img" aria-label="Photo of a hiker in a knitted hat crouching beside a campfire by a lake">
      <defs>
        <linearGradient id="campfire" x1="0" y1="0" x2="0" y2="1">
          <stop offset="0" stop-color="#6f8aa6"/>
          <stop offset=".45" stop-color="#4e5d6c"/>
          <stop offset=".75" stop-color="#5a4432"/>
          <stop offset="1" stop-color="#3a3028"/>
        </linearGradient>
      </defs>
      <rect width="386" height="546" fill="url(#campfire)"/>
    </svg>

    <div class="abs rate-card">
      <div class="rate" style="top:34px;"><span>Traveldirectory</span><span class="rate__price">€ 100/<small>year</small></span></div>
      <div class="rate" style="top:55px;"><span>Textlink</span><span class="rate__price">€ 250/<small>year</small></span></div>
      <div class="rate" style="top:76px;"><span>Advertorials<span class="rate__small">(max 3 links)</span></span><span class="rate__price">€ 500</span></div>
      <div class="rate rate--note" style="top:97px;"><span>Sidebars</span><span class="rate__price rate__note">Please ask for current pricing</span></div>
      <div class="rate rate--note" style="top:118px;"><span>Banners</span><span class="rate__price rate__note">Please ask for current pricing</span></div>
      <div class="rate rate--header" style="top:145px;">Social Shares</div>
      <div class="rate" style="top:172px;"><span>Friendbook</span><span class="rate__price">€ 150</span></div>
      <div class="rate" style="top:193px;"><span>Snapgram</span><span class="rate__price">€ 100</span></div>
      <div class="rate" style="top:214px;"><span>Chirper</span><span class="rate__price">€ 50</span></div>
      <div class="rate" style="top:235px;"><span>Reviews</span><span class="rate__price">€ 250</span></div>
      <div class="rate" style="top:256px;"><span>Tubecast video</span><span class="rate__price">€ 250</span></div>
      <div class="rate rate--wide" style="top:277px;"><span>Videography using drones</span><span class="rate__price">€ 1,000</span></div>
    </div>
  </section>

  <!-- Page: sponsorship -->
  <section class="page page--right">
    <svg class="page__frame" viewBox="0 0 387 546" preserveAspectRatio="none" aria-hidden="true">
      <defs>
        <linearGradient id="beach" x1="0" y1="0" x2="0" y2="1">
          <stop offset="0" stop-color="#6d7a86"/>
          <stop offset=".5" stop-color="#a9b0b4"/>
          <stop offset="1" stop-color="#d4d2cc"/>
        </linearGradient>
        <linearGradient id="floorGreyR" x1="0" y1="0" x2="0" y2="1">
          <stop offset="0" stop-color="#e6e6e6"/>
          <stop offset="1" stop-color="#bdbdbd"/>
        </linearGradient>
      </defs>
      <rect x="0" y="0" width="387" height="130" fill="url(#beach)" role="img" aria-label="Photo of penguins on a rocky beach"/>
      <path d="M0,92 C110,62 260,54 387,60 L387,68 C260,62 110,70 0,100 Z" fill="#fff" opacity=".85"/>
      <path d="M0,100 C110,70 260,62 387,68 L387,80 C260,74 110,82 0,112 Z" fill="var(--blue)"/>
      <path d="M0,112 C110,82 260,74 387,80 L387,546 L0,546 Z" fill="#fff"/>
      <path d="M0,448 C130,500 270,512 387,498 L387,546 L0,546 Z" fill="url(#floorGreyR)"/>
      <path d="M0,448 C130,500 270,512 387,498 L387,508 C270,522 130,514 0,464 Z" fill="var(--blue)"/>
      <path d="M0,472 C130,522 270,532 387,518 L387,521 C270,535 130,526 0,476 Z" fill="#9a9a9a"/>
    </svg>

    <h2 class="abs sponsor-title">Sponsorship Opportunities</h2>
    <p class="abs body-copy sponsor-intro">Bolderwijk has a large online interactive community through its readers and social networks that provides a perfect venue to showcase your brand or destination to a highly engaged online audience of travel enthusiasts.</p>
    <p class="abs sponsor-lead">Check out some of the things we can do for you.</p>

    <ul class="abs services">
      <li class="service">
        <h4 class="service__title"><span class="service__dot"></span>Travel Writing</h4>
        <p class="body-copy">Yes please! Digital Storytelling our core business. About independent &amp; off the beaten path travel. About exciting cities, with their buzzing street life, wild nightlife and unbeatable attractions. About otherworldly landscapes and awe-inspiring natural wonders. Near and afar.</p>
      </li>
      <li class="service">
        <h4 class="service__title"><span class="service__dot"></span>Press &amp; Fam Trips</h4>
        <p class="body-copy">The only thing we love more than experiencing new places is sharing the destinations with our readers. Our travel journalists are invited by tourist offices, airline companies, hotel brands and other partners. In 2016 for example our journalists went to Peru, Norway, South Africa, Costa Rica, Thailand and Spitsbergen.</p>
      </li>
      <li class="service">
        <h4 class="service__title"><span class="service__dot"></span>Reviews / Sponsorship</h4>
        <p class="body-copy">We love reviews! They give us a chance to let our readers know about unique products for the experiential traveler. We’d love to write an honest review for your app, product, hotel or anything else you can think of!</p>
      </li>
      <li class="service">
        <h4 class="service__title"><span class="service__dot"></span>Travel directory</h4>
        <p class="body-copy">Are you the owner of a small romantic B&amp;B in Italy? Or of that cool rafting company in Bali? Or do you have an excellent restaurant on Isla Sol? We invented our unique traveldirectory for local companies, where we match accommodations, attractions, tours, travelcompanies and restaurants to a specific destination.</p>
      </li>
      <li class="service">
        <h4 class="service__title"><span class="service__dot"></span>Advertising</h4>
        <p class="body-copy">Advertorials, SEO articles, sidebars, banners, social media promotion. We have a lot of interesting advertising opportunities to help your business market its products and services to a target audience and help you expand your brand awareness.</p>
      </li>
      <li class="service">
        <h4 class="service__title"><span class="service__dot"></span>Photography</h4>
        <p class="body-copy">It’s no secret that stunning images are one of the best and easiest ways to showcase your brand or destination. We offer a selection of photography services that help enhance your brands website and social networks.</p>
      </li>
      <li class="service">
        <h4 class="service__title"><span class="service__dot"></span>Travelvlogs</h4>
        <p class="body-copy">Professionally produced and edited Tubecast videos. Showcase your destination through the eyes of a world traveler!</p>
      </li>
      <li class="service">
        <h4 class="service__title"><span class="service__dot"></span>Videography using drones</h4>
        <p class="body-copy">Our state of the art drone footages will blow your mind.</p>
      </li>
    </ul>

    <p class="abs pricing-note">Please ask for current pricing</p>
  </section>

</main>
</body>
</html>
```